Business card and stationary package

Travel management company looking for designs for single sided business cards, letterhead and envelope. Looking for contemporary designs using our existing logo. Design should clean, not trendy, no gradation of colors and no graphic other than the icon from the logo. Nothing complicated or difficult to read. Should be a crisp design using blue, gray and black colors only.
Letterhead should include a Word template and PDF template.
Business cards are one sided as the reverse will be dynamic images in our company portfolio of images.
We will use the same designer periodically for design projects using the same style guide for upcoming projects as well. Prefer working with designer that will assist with website, brochures and other marketing materials.

Logo Colors and Font:
Blue: 2189c6 Color Hex
Gray: 666666 Color Hex 60% Black
Black: 100% Black
Font: Century Gothic

Target Market(s)

business-to-business

Industry/Entity Type

Travel Industry

Contact Information for Business Card

Sample information for business cards will be:

Daniel Fenwick
Managing Partner

Harborline Journey Services, Inc.
274 Alder Lane, Suite 3621
Alder Falls, ME 04099

207-555-0148 Direct Dial
207-555-0193 Fax

daniel@harborlinejourney.net
www.harborlinejourney.net

Font styles to use
Sans Serif

Requirements
Must have
• Clean, crisp design, easy to ready, memorable.
Nice to have
• We tend to like dynamic designs that are simple, not trendy, contemporary and easy to read.
Should not have
• no gradation of colors and no graphic other than the icon from the logo, no background images
• **Note that the background should only be white. No black/gary backgrounds or graded colors**

```html
<!DOCTYPE html>
<html lang="en">
<head>
<meta charset="utf-8">
<title>Harborline Journey Services – Business Card</title>
<link rel="stylesheet" href="https://fonts.googleapis.com/css2?family=Questrial&family=Source+Sans+3:wght@400;600&display=swap">
<style>
  :root {
    --brand-blue: #2189c6;
    --brand-gray: #666666;
    --text-gray: #555555;
    --card-white: #ffffff;
    --stage: #141414;
  }
  html, body {
    margin: 0;
    padding: 0;
    width: 1200px;
    height: 900px;
    overflow: hidden;
    background: var(--stage);
  }
  .stage {
    position: relative;
    width: 1200px;
    height: 900px;
    font-family: "Source Sans 3", "Myriad Pro", sans-serif;
  }
  .card {
    position: absolute;
    top: 306px;
    height: 271px;
    background: var(--card-white);
    border-radius: 12px;
  }
  .card--front { left: 149px; width: 439px; }
  .card--back  { left: 608px; width: 441px; }

  /* front: brand block */
  .brand-block {
    position: absolute;
    left: 54px;
    top: 56px;
    width: 124px;
    text-align: center;
  }
  .brand-block__dot {
    display: block;
    width: 72px;
    height: 72px;
    margin: 0 auto 14px;
    border-radius: 50%;
    background: var(--brand-blue);
  }
  .brand-block__name {
    font-family: "Questrial", "Century Gothic", sans-serif;
    font-size: 17px;
    letter-spacing: 0.5px;
    color: var(--brand-blue);
  }

  /* front: details */
  .details {
    position: absolute;
    left: 217px;
    top: 54px;
    color: var(--text-gray);
    font-size: 13px;
    line-height: 15.6px;
  }
  .details__name {
    margin: 0;
    font-size: 15.5px;
    font-weight: 600;
    line-height: 18px;
    color: var(--brand-blue);
  }
  .details__title { margin: 0 0 12px; }
  .details__address { margin: 0 0 9px; font-style: normal; }
  .contact-list { list-style: none; margin: 0; padding: 0; }
  .contact-list li { display: flex; align-items: center; height: 15.8px; }
  .contact-list svg {
    width: 9px;
    height: 9px;
    margin: 0 7px 0 0;
    fill: var(--brand-blue);
    flex: none;
  }

  /* back: wordmark */
  .wordmark {
    position: absolute;
    left: 100px;
    top: 90px;
    display: flex;
    align-items: center;
  }
  .wordmark__dot {
    width: 54px;
    height: 54px;
    border-radius: 50%;
    background: var(--brand-blue);
    margin-right: 14px;
  }
  .wordmark__text {
    font-family: "Questrial", "Century Gothic", sans-serif;
    color: var(--brand-gray);
    line-height: 1;
  }
  .wordmark__main { display: block; font-size: 28px; letter-spacing: 1px; }
  .wordmark__sub { display: block; font-size: 9.5px; letter-spacing: 2.6px; margin-top: 3px; }
</style>
</head>
<body>
<main class="stage">
  <section class="card card--front" aria-label="Business card front">
    <div class="brand-block">
      <span class="brand-block__dot"></span>
      <span class="brand-block__name">Harborline</span>
    </div>
    <div class="details">
      <p class="details__name">Daniel Fenwick</p>
      <p class="details__title">Managing Partner</p>
      <address class="details__address">
        Harborline Journey Services, Inc.<br>
        274 Alder Lane, Suite 3621<br>
        Alder Falls, ME 04099
      </address>
      <ul class="contact-list">
        <li><svg viewBox="0 0 10 10"><path d="M2 0.5 L3.6 2.6 L2.8 3.6 Q4 6 6.4 7.2 L7.4 6.4 L9.5 8 L8.3 9.5 Q4.5 9.3 2.2 6.8 Q0.5 4.5 0.5 1.7 Z"/></svg>207-555-0148</li>
        <li><svg viewBox="0 0 10 10"><rect x="2.5" y="0.5" width="5" height="3"/><rect x="0.5" y="3.5" width="9" height="6" rx="1"/></svg>207-555-0193</li>
        <li><svg viewBox="0 0 10 10"><path d="M0.5 2 H9.5 V8.5 H0.5 Z M0.5 2 L5 5.5 L9.5 2" /></svg>daniel@harborlinejourney.net</li>
        <li><svg viewBox="0 0 10 10"><circle cx="5" cy="5" r="4.5"/></svg>www.harborlinejourney.net</li>
      </ul>
    </div>
  </section>

  <section class="card card--back" aria-label="Business card back">
    <div class="wordmark">
      <span class="wordmark__dot"></span>
      <span class="wordmark__text">
        <span class="wordmark__main">HARBORLINE</span>
        <span class="wordmark__sub">JOURNEY SERVICES</span>
      </span>
    </div>
  </section>
</main>
</body>
</html>
```